Brightmoor Leisure Works Investor Brochure

Start Up Company Brightmoor Leisure Works requires 4 page A4 size brochure outlining and detailing new product. Draft layout attached. Information and points of difference included. Company logo and graphics attached. Final design should sell to investors.
Industry/Entity Type
It Company

```html
<!DOCTYPE html>
<html lang="en">
<head>
<meta charset="utf-8">
<title>Brightmoor Leisure Works – Airports Across Australia</title>
<link href="https://fonts.googleapis.com/css2?family=Roboto+Condensed:wght@300;400;700&display=swap" rel="stylesheet">
<style>
  :root {
    --green: #9bbd4e;
    --blue-light: #1cb3ea;
    --blue-dark: #0a8ed6;
    --cell: #1d93d8;
    --text-grey: #555a5e;
    --page-line: #cfcfcf;
    --white: #ffffff;
  }
  * { margin: 0; padding: 0; box-sizing: border-box; }
  html, body { width: 1000px; height: 1200px; overflow: hidden; background: var(--white); }
  body { position: relative; font-family: "Roboto Condensed", "Arial Narrow", sans-serif; }

  .page {
    position: absolute; left: 123px; top: 72px; width: 748px; height: 1057px;
    border: 1px solid var(--page-line); background: var(--white);
  }
  .abs { position: absolute; }

  .headline-band { left: 204px; top: 161px; }
  .headline {
    left: 230px; top: 179px; color: var(--white); font-weight: 700; line-height: 1;
    text-transform: uppercase; letter-spacing: -0.3px;
  }
  .headline .small { display: block; font-size: 20px; margin-bottom: 4px; }
  .headline .large { display: block; font-size: 27px; line-height: 27px; }

  .route-map {
    left: 348px; top: 283px; width: 366px; height: 228px;
    background: radial-gradient(ellipse at 50% 45%, #a3c559 0%, var(--green) 75%, #c9dc9f 100%);
    border-radius: 40% 36% 30% 34% / 44% 40% 36% 40%;
  }

  .selling-points { left: 224px; top: 520px; width: 340px; list-style: none; }
  .selling-points li {
    position: relative; padding-left: 19px; color: var(--text-grey);
    font-size: 12px; font-weight: 700; line-height: 19px; margin-bottom: 3.5px;
    text-align: justify; letter-spacing: 0.2px;
  }
  .selling-points li::before {
    content: ""; position: absolute; left: 0; top: 6px; width: 6px; height: 6px;
    background: var(--green);
  }

  .traffic-band { left: 206px; top: 690px; }
  .traffic-title {
    left: 385px; top: 712px; color: var(--white); font-weight: 700;
    font-size: 21px; line-height: 24px;
  }

  .kiosk-render {
    left: 200px; top: 700px; width: 150px; height: 336px;
    background: linear-gradient(180deg, #2a3a55 0%, #1f4f96 45%, #2a6cc4 80%, #1b2533 100%);
    border-radius: 8px 26px 2px 2px;
  }

  .demand-note {
    left: 385px; top: 829px; color: var(--text-grey); font-weight: 700; font-size: 13px;
  }

  .passenger-table {
    left: 386px; top: 859px; width: 405px;
    display: grid; grid-template-columns: 198px 204px; column-gap: 3px; row-gap: 1px;
  }
  .passenger-table .cell {
    display: flex; justify-content: space-between; align-items: center;
    background: var(--cell); color: var(--white); font-size: 10px; font-weight: 300;
    height: 18.7px; padding: 0 13px 0 22px; letter-spacing: 0.2px;
  }
  .passenger-table .cell:nth-child(2n) { padding: 0 14px 0 12px; }
</style>
</head>
<body>
<div class="page"></div>

<svg class="abs headline-band" width="590" height="122" viewBox="0 0 590 122" aria-hidden="true">
  <polygon points="0,0 586,0 586,110 192,92 192,107 0,118" fill="var(--green)"/>
</svg>
<h1 class="abs headline"><span class="small">Coming soon to</span><span class="large">Airports across<br>Australia</span></h1>

<div class="abs route-map" role="img" aria-label="Map of Australia marking planned kiosk airport locations"></div>

<ul class="abs selling-points">
  <li>Current technology allows up to 10,000 encrypted digital movies to be stored on a kiosk.</li>
  <li>Multiple customers can simultaneously browse and rent movies on the Kiosks FREE Wifi</li>
  <li>Travellers are always killing time waiting to board there flight.</li>
  <li>Perfect time to browse movies.</li>
  <li>Target of 1 million transactions in the first 12 months</li>
</ul>

<svg class="abs traffic-band" width="586" height="120" viewBox="0 0 586 120" aria-hidden="true">
  <defs>
    <linearGradient id="bandBlue" x1="0" y1="0" x2="1" y2="0">
      <stop offset="0" stop-color="var(--blue-light)"/>
      <stop offset="1" stop-color="var(--blue-dark)"/>
    </linearGradient>
  </defs>
  <polygon points="0,0 586,0 586,111 379,118 196,90 196,118 0,118" fill="url(#bandBlue)"/>
</svg>
<div class="abs kiosk-render" role="img" aria-label="Movie rental kiosk product render"></div>
<h2 class="abs traffic-title">145,000,000+ Passenger Movements<br>For YE Feb 2014. Up 3.1% on 2013</h2>

<p class="abs demand-note">New Airport announced for Western Sydney to cope with increase demand.</p>

<div class="abs passenger-table">
  <div class="cell"><span>SYDNEY</span><span>38 437 737</span></div><div class="cell"><span>MELBOURNE</span><span>30 484 074</span></div>
  <div class="cell"><span>BRISBANE</span><span>21 570 625</span></div><div class="cell"><span>PERTH</span><span>12 989 955</span></div>
  <div class="cell"><span>ADELAIDE</span><span>7 460 471</span></div><div class="cell"><span>GOLD COAST</span><span>5 789 986</span></div>
  <div class="cell"><span>CAIRNS</span><span>4 293 485</span></div><div class="cell"><span>CANBERRA</span><span>2 931 006</span></div>
  <div class="cell"><span>HOBART</span><span>2 098 416</span></div><div class="cell"><span>DARWIN</span><span>2 023 665</span></div>
  <div class="cell"><span>TOWNSVILLE</span><span>1 543 457</span></div><div class="cell"><span>LAUNCESTON</span><span>1 267 589</span></div>
  <div class="cell"><span>WILLIAMTOWN</span><span>1 208 188</span></div><div class="cell"><span>MACKAY</span><span>1 083 805</span></div>
  <div class="cell"><span>SUNSHINE COAST</span><span>891 300</span></div><div class="cell"><span>KARRATHA</span><span>763 137</span></div>
  <div class="cell"><span>ROCKHAMPTON</span><span>694 368</span></div><div class="cell"><span>ALICE SPRINGS</span><span>667 383</span></div>
  <div class="cell"><span>GLADSTONE</span><span>500 429</span></div><div class="cell"><span>PORT HEDLAND</span><span>491 274</span></div>
</div>
</body>
</html>
```